" A empresa desenvolve projetos residenciais, corporativos entre outros para público de médio/alto padrão, bem como acompanhamento/gerenciamento de obra e contam com parceiros na execução do projeto... "

```html
<!DOCTYPE html>
<html lang="pt-BR">
<head>
<meta charset="utf-8">
<title>Papel timbrado — Clara Novaes</title>
<link href="https://fonts.googleapis.com/css2?family=Montserrat:wght@400;500;600&display=swap" rel="stylesheet">
<style>
  :root {
    --backdrop: #a9a9a9;
    --paper: #ffffff;
    --ink: #2b2b2b;
    --ink-soft: #6a6a6a;
    --gold: #e3b43a;
    --line: #cfcfcf;
    --faint: #f1f1f1;
  }
  * { margin: 0; padding: 0; box-sizing: border-box; }
  html, body { width: 1200px; height: 1200px; overflow: hidden; }
  body {
    background: var(--backdrop);
    font-family: "Montserrat", sans-serif;
    color: var(--ink);
    position: relative;
  }
  .letterhead {
    position: absolute;
    left: 225px; top: 70px;
    width: 750px; height: 1060px;
    background: var(--paper);
    box-shadow: 0 10px 30px rgba(0,0,0,.25);
    overflow: hidden;
  }
  .site-bar {
    position: absolute; top: 58px; right: 60px; left: 330px;
    display: flex; align-items: center; gap: 14px;
  }
  .site-bar .rule { flex: 1; height: 1px; background: var(--line); }
  .site-bar .url { font-size: 11px; letter-spacing: 1.5px; color: var(--ink-soft); }
  .corner-decor {
    position: absolute; top: 80px; right: 40px;
    width: 330px; height: 180px;
    background: radial-gradient(circle at 40% 50%, var(--faint), #fafafa 70%, transparent);
  }
  .brand {
    position: absolute; top: 110px; left: 70px;
    display: flex; align-items: center; gap: 14px;
  }
  .brand .mark { width: 14px; height: 14px; background: var(--gold); }
  .brand .name { font-size: 30px; font-weight: 500; color: var(--ink); letter-spacing: 1px; }
  .brand-tag {
    position: absolute; top: 156px; left: 98px;
    font-size: 10px; letter-spacing: 2px; text-transform: uppercase; color: var(--gold);
  }
  .letter-body {
    position: absolute; top: 320px; left: 70px; width: 470px;
    font-size: 13px; line-height: 1.55; color: var(--ink);
  }
  .letter-body p { margin-bottom: 16px; }
  .signature {
    position: absolute; top: 560px; right: 80px;
    width: 170px; height: 50px;
    background: linear-gradient(90deg, #ececec, #dcdcdc);
    border-radius: 4px;
  }
  .pattern-band {
    position: absolute; top: 630px; left: 0; right: 0; height: 230px;
    background: linear-gradient(180deg, #ffffff, var(--faint) 50%, #ffffff);
  }
  .contacts {
    position: absolute; top: 890px; left: 70px;
    list-style: none; font-size: 11px; color: var(--ink-soft); line-height: 1.9;
  }
  .contacts li { display: flex; align-items: center; gap: 8px; }
  .contacts svg { width: 11px; height: 11px; fill: var(--gold); flex: none; }
  .footer-rule {
    position: absolute; bottom: 55px; left: 70px; right: 60px;
    height: 1px; background: var(--line);
  }
</style>
</head>
<body>
  <main class="letterhead">
    <div class="site-bar"><span class="rule"></span><span class="url">www.claranovaes.com.br</span></div>
    <div class="corner-decor" role="img" aria-label="Desenho arquitetônico suave em cinza claro"></div>

    <div class="brand"><span class="mark"></span><span class="name">Clara Novaes</span></div>
    <div class="brand-tag">Arquitetura &amp; Interiores</div>

    <section class="letter-body">
      <p>Prezados, apresentamos a seguir a proposta de desenvolvimento do projeto de interiores para a nova residência, contemplando o estudo preliminar, o anteprojeto e o detalhamento executivo, além do acompanhamento técnico de cada etapa da obra.</p>
      <p>Todas as soluções consideram o uso racional dos espaços, a escolha criteriosa de materiais e a integração com nossos parceiros de execução, garantindo qualidade, prazo e um resultado alinhado ao perfil de cada cliente.</p>
      <p>Ficamos à disposição para agendar uma reunião e apresentar os detalhes da proposta. Atenciosamente.</p>
    </section>

    <div class="signature" role="img" aria-label="Assinatura manuscrita"></div>

    <div class="pattern-band" role="img" aria-label="Padrão geométrico de linhas em ziguezague, cinza muito claro"></div>

    <ul class="contacts">
      <li><svg viewBox="0 0 24 24"><path d="M6.6 10.8a15 15 0 0 0 6.6 6.6l2.2-2.2a1 1 0 0 1 1-.25 11.4 11.4 0 0 0 3.6.57 1 1 0 0 1 1 1V20a1 1 0 0 1-1 1A17 17 0 0 1 3 4a1 1 0 0 1 1-1h3.5a1 1 0 0 1 1 1c0 1.25.2 2.45.57 3.6a1 1 0 0 1-.25 1z"/></svg>(11) 4002-1870 / 98715-2204</li>
      <li><svg viewBox="0 0 24 24"><path d="M6.6 10.8a15 15 0 0 0 6.6 6.6l2.2-2.2a1 1 0 0 1 1-.25 11.4 11.4 0 0 0 3.6.57 1 1 0 0 1 1 1V20a1 1 0 0 1-1 1A17 17 0 0 1 3 4a1 1 0 0 1 1-1h3.5a1 1 0 0 1 1 1c0 1.25.2 2.45.57 3.6a1 1 0 0 1-.25 1z"/></svg>(11) 99120-4587</li>
      <li><svg viewBox="0 0 24 24"><path d="M2 5h20v14H2zm2 2v.5l8 5 8-5V7z"/></svg>contato@claranovaes.com.br</li>
      <li><svg viewBox="0 0 24 24"><path d="M12 2a7 7 0 0 0-7 7c0 5.25 7 13 7 13s7-7.75 7-13a7 7 0 0 0-7-7zm0 9.5A2.5 2.5 0 1 1 12 6.5a2.5 2.5 0 0 1 0 5z"/></svg>Rua das Acácias, 210 – Centro – Campinas/SP</li>
    </ul>

    <div class="footer-rule"></div>
  </main>
</body>
</html>
```